Zielgruppe
Verein
Angebote:
Beratungsangebote
Bildungsangebote
Kulturelle Verantaltungen/Interkulturelle Veranstaltungen
Generationsübergreifende Angebote
Zielgruppe:
alle Menschen
Themen:
Entwicklung
Charakter
Individualität
Selbstbewusstsein
Auszug aus der Vereinssatzung:
[...] Durch ein möglichst vielfältiges Angebot sollen Menschen allen Alters die Chance haben, eine selbstständige, sich selbst akzeptierende, selbstbewusste, zielstrebige Persönlichkeit herauszubilden bzw. prozesshaft lebenslang zu entwickeln. Wir wollen Menschen zudem unterstützen, Fähigkeiten und Kompetenzen zu entwickeln, Wirklichkeiten zu erkennen, andere Sichtweisen einzunehmen sowie persönliche und berufliche Möglichkeiten zu sehen, um für sich (Zukunfts-)Perspektiven zu formulieren.
Wir sehen den Zweck des Vereins im Längsschnitt darin, dass eine inklusive Gesellschaft, die aus Persönlichkeiten mit Perspektiven besteht, das demokratische Staatswesen fördert und durch Respekt untereinander weitere Rechte auf Gleichstellung formuliert, verankert und umsetzt.
Aufgabenstellung
Wichtig ist die graphische Umsetzung der Begriffe
Persönlichkeit und
Perspektiven.

```html
<!DOCTYPE html>
<html lang="de">
<head>
<meta charset="utf-8">
<title>KaReV – Geschäftsausstattung</title>
<link rel="stylesheet" href="https://fonts.googleapis.com/css2?family=Open+Sans:wght@400;600;700&display=swap">
<style>
  :root {
    --ink: #0f1c24;
    --paper: #ffffff;
    --stage: #e8e5e0;
    --text: #2a2f33;
    --muted: #7b8389;
    --accent: #e2412e;
    --rule: #c9ced2;
  }
  * { box-sizing: border-box; margin: 0; padding: 0; }
  html, body { width: 1200px; height: 789px; overflow: hidden; }
  body {
    background: var(--stage);
    font-family: "Open Sans", Arial, sans-serif;
    color: var(--text);
    position: relative;
  }
  .sheet { position: absolute; background: var(--paper); box-shadow: 0 2px 8px rgba(0,0,0,.12); }

  /* brand lockup */
  .brand { display: flex; flex-direction: column; align-items: flex-start; }
  .brand-row { display: flex; align-items: center; gap: 6px; }
  .brand-dot { width: 16px; height: 16px; border-radius: 50%; background: var(--accent); }
  .brand-name { font-weight: 700; font-size: 22px; letter-spacing: .5px; color: var(--ink); line-height: 1; }
  .brand-claim { font-size: 7px; font-weight: 600; color: var(--ink); margin: 3px 0 0 22px; }
  .on-dark .brand-name, .on-dark .brand-claim { color: var(--paper); }

  /* letterhead */
  .letterhead { left: 40px; top: 40px; width: 340px; height: 481px; padding: 30px 30px 20px 34px; font-size: 6.2px; line-height: 1.55; }
  .letterhead .brand { position: absolute; right: 30px; top: 28px; }
  .letter-sender { margin-top: 62px; font-size: 4.8px; color: var(--muted); }
  .letter-recipient { margin-top: 4px; font-weight: 600; font-size: 6.5px; line-height: 1.45; }
  .letter-date { text-align: right; margin-top: 18px; }
  .letter-body p { margin-top: 9px; }
  .letter-signature { margin-top: 8px; height: 26px; }
  .letter-footer { position: absolute; left: 34px; right: 30px; bottom: 20px; display: flex; justify-content: space-between; border-top: .5px solid var(--rule); padding-top: 6px; font-size: 4.8px; color: var(--muted); line-height: 1.5; }

  /* folder cover */
  .cover { left: 400px; top: 40px; width: 340px; height: 481px; background: var(--ink); }
  .cover .brand { position: absolute; left: 104px; top: 150px; }
  .cover .brand-name { font-size: 30px; }
  .cover .brand-dot { width: 22px; height: 22px; }
  .cover .brand-claim { font-size: 8px; margin-left: 28px; }
  .cover-web { position: absolute; right: 24px; bottom: 22px; color: var(--paper); font-size: 7px; letter-spacing: .6px; }

  /* envelope */
  .envelope { left: 770px; top: 40px; width: 390px; height: 196px; }
  .envelope .brand { position: absolute; right: 26px; top: 22px; }
  .envelope-address { position: absolute; left: 34px; bottom: 26px; font-size: 8px; line-height: 1.45; font-weight: 600; }
  .envelope-sender { font-size: 5.5px; font-weight: 400; color: var(--muted); border-bottom: .5px solid var(--rule); padding-bottom: 2px; margin-bottom: 4px; }

  /* business cards */
  .card { width: 190px; height: 112px; }
  .card-back { left: 770px; top: 270px; background: var(--ink); display: flex; align-items: center; justify-content: center; }
  .card-back .brand-name { font-size: 20px; }
  .card-front { left: 980px; top: 270px; padding: 12px 14px; font-size: 5.6px; line-height: 1.5; }
  .card-front .brand { align-items: center; }
  .card-front .brand-name { font-size: 15px; }
  .card-front .brand-dot { width: 12px; height: 12px; }
  .card-front .brand-claim { font-size: 5px; margin-left: 18px; }
  .card-person { text-align: center; margin-top: 7px; }
  .card-name { font-weight: 700; font-size: 8px; color: var(--ink); }
  .card-role { color: var(--muted); }
  .card-contact { display: flex; justify-content: space-between; margin-top: 6px; }
  .card-contact dl { display: grid; grid-template-columns: auto auto; column-gap: 3px; }
  .card-contact dt { font-weight: 700; }
</style>
</head>
<body>

<section class="sheet letterhead" aria-label="Briefbogen">
  <div class="brand">
    <div class="brand-row"><span class="brand-dot"></span><span class="brand-name">KaReV</span></div>
    <span class="brand-claim">Kreis aller Reifewege e.V.</span>
  </div>
  <p class="letter-sender">KaReV · Straßenname 10 · 12345 Stadtname</p>
  <p class="letter-recipient">Herr Mustermann<br>Street Name 99-1<br>12345 City<br>Germany</p>
  <p class="letter-date">Stadtname, 10. Januar 2016</p>
  <div class="letter-body">
    <p>Sehr geehrter Herr Mustermann,</p>
    <p>Lorem ipsum dolor sit amet, consectetur adipiscing elit, sed do eiusmod tempor incididunt ut labore et dolore magna aliqua. Ut enim ad minim veniam, quis nostrud exercitation ullamco laboris.</p>
    <p>Duis aute irure dolor in reprehenderit in voluptate velit esse cillum dolore eu fugiat nulla pariatur.</p>
    <p>Excepteur sint occaecat cupidatat non proident, sunt in culpa qui officia deserunt mollit anim id est laborum.</p>
    <p>Mit freundlichen Grüßen</p>
  </div>
  <svg class="letter-signature" width="60" height="26" viewBox="0 0 60 26" aria-hidden="true">
    <path d="M4 20 C12 8, 18 24, 26 14 S40 6, 46 18 L52 12" fill="none" stroke="var(--ink)" stroke-width="1"/>
  </svg>
  <footer class="letter-footer">
    <p>Kreis aller Reifewege e.V.<br>Straßenname 10<br>12345 Stadtname</p>
    <p>Tel +49 0123 456789<br>Fax +49 0123 456780<br>Mail info@yourwebsite.de</p>
    <p>Bank Musterbank<br>IBAN DE00 0000 0000<br>BIC MUSTDEXX</p>
  </footer>
</section>

<section class="sheet cover on-dark" aria-label="Mappe">
  <div class="brand">
    <div class="brand-row"><span class="brand-dot"></span><span class="brand-name">KaReV</span></div>
    <span class="brand-claim">Kreis aller Reifewege e.V.</span>
  </div>
  <p class="cover-web">www.yourwebsite.de</p>
</section>

<section class="sheet envelope" aria-label="Briefumschlag">
  <div class="brand">
    <div class="brand-row"><span class="brand-dot"></span><span class="brand-name">KaReV</span></div>
    <span class="brand-claim">Kreis aller Reifewege e.V.</span>
  </div>
  <div class="envelope-address">
    <p class="envelope-sender">KaReV, Straßenname 10, 12345 Stadtname</p>
    <p>Herr Mustermann<br>Street Name 99-1<br>12345 City<br>Germany</p>
  </div>
</section>

<section class="sheet card card-back on-dark" aria-label="Visitenkarte Rückseite">
  <div class="brand">
    <div class="brand-row"><span class="brand-dot"></span><span class="brand-name">KaReV</span></div>
    <span class="brand-claim">Kreis aller Reifewege e.V.</span>
  </div>
</section>

<section class="sheet card card-front" aria-label="Visitenkarte Vorderseite">
  <div class="brand">
    <div class="brand-row"><span class="brand-dot"></span><span class="brand-name">KaReV</span></div>
    <span class="brand-claim">Kreis aller Reifewege e.V.</span>
  </div>
  <div class="card-person">
    <p class="card-name">Max Mustermann</p>
    <p class="card-role">CEO</p>
    <p>Straßenname 10 | 12345 Stadtname</p>
  </div>
  <div class="card-contact">
    <dl><dt>Tel</dt><dd>+49 0123 456789</dd><dt>Mail</dt><dd>info@yourwebsite.de</dd></dl>
    <dl><dt>Fax</dt><dd>+49 0123 456780</dd><dt>Web</dt><dd>www.yourwebsite.de</dd></dl>
  </div>
</section>

</body>
</html>
```